Bright Path Attorneys Billboard Design for Personal Injury Law Firm

Need a billboard design that we can use for different versions. 1400px X 400px jpeg or png
I have attached the logo and the attorney for the billboard. Attorney Marla Benning
Here is a link to our current website brightpathlegalgroup.example

HEADLINE: HIT BY A TRUCK?
SUBHEAD: NO FEE. BIG FIGHT.
877-GRANTLY

HEADLINE: ACCIDENT?
SUBHEAD: NO FEE, UNLESS WE WIN!
877-GRANTLY

HEADLINE: BIG TRUCK. BIG CASE.
SUBHEAD: YOU PAY $0 UPFRONT
877-GRANTLY

Target Market(s)

People in Car Accident

Industry/Entity Type

Personal Injury Attorneys

```html
<!DOCTYPE html>
<html lang="en">
<head>
<meta charset="utf-8">
<title>Bright Path Attorneys – Billboard Set</title>
<link href="https://fonts.googleapis.com/css2?family=Bebas+Neue&family=Montserrat:wght@700;800&display=swap" rel="stylesheet">
<style>
  :root{
    --page:#e6e6e6;
    --board:#05080f;
    --green:#9cff00;
    --white:#ffffff;
    --yellow:#ffc20e;
    --silver:#c9c9c9;
  }
  *{margin:0;padding:0;box-sizing:border-box}
  html,body{width:1200px;height:1137px;overflow:hidden;background:var(--page)}
  body{position:relative;font-family:"Montserrat",sans-serif}

  .billboard{position:absolute;left:104px;width:992px;height:284px;background:var(--board);overflow:hidden}
  .billboard--truck-fight{top:91px}
  .billboard--accident{top:438px}
  .billboard--big-case{top:762px}

  .scene{position:absolute;left:0;top:0;width:330px;height:224px}
  .scene--truck{background:linear-gradient(90deg,rgba(120,20,28,.95) 0%,rgba(90,30,40,.85) 35%,rgba(45,55,75,.6) 65%,rgba(5,8,15,0) 100%),linear-gradient(180deg,#6d86a6 0%,#3a3f4e 55%,#1a1c24 100%)}
  .scene--car{background:linear-gradient(90deg,rgba(240,236,240,.95) 0%,rgba(190,185,200,.8) 30%,rgba(60,66,82,.6) 62%,rgba(5,8,15,0) 100%),linear-gradient(180deg,#e9e4ea 0%,#8d8a98 55%,#3a3a44 100%)}

  .headline{position:absolute;left:0;top:0;width:992px;height:224px;overflow:visible}
  .headline text{font-family:"Bebas Neue",sans-serif}

  .rule{position:absolute;left:0;top:223px;width:796px;height:2px;background:var(--green)}
  .phone{position:absolute;left:58px;top:228px;font-weight:800;font-size:44px;line-height:54px;color:var(--white);letter-spacing:.5px}
  .web{position:absolute;left:498px;top:239px;font-weight:700;font-size:21px;line-height:30px;color:var(--green)}

  .brand{position:absolute;left:694px;top:16px;display:flex;align-items:center;gap:12px}
  .brand__dot{width:40px;height:40px;border-radius:50%;background:var(--green)}
  .brand__name{font-weight:700;font-size:19px;line-height:21px;color:var(--white);letter-spacing:1.5px;border-left:1px solid transparent}

  .attorney{position:absolute;left:792px;top:70px;width:195px;height:214px;border-radius:90px 90px 0 0;background:linear-gradient(180deg,#b88a5e 0%,#8a6a52 35%,#1d2a4a 62%,#16203a 100%)}
</style>
</head>
<body>

<section class="billboard billboard--truck-fight">
  <div class="scene scene--truck" role="img" aria-label="Photo of a red semi truck seen from a low angle"></div>
  <svg class="headline" viewBox="0 0 992 224">
    <text x="185" y="102" font-size="83" fill="var(--white)" textLength="378" lengthAdjust="spacingAndGlyphs">HIT BY A TRUCK?</text>
    <text x="185" y="189" font-size="107" fill="var(--white)" textLength="214" lengthAdjust="spacingAndGlyphs">NO FEE.</text>
    <text x="422" y="189" font-size="107" fill="var(--green)" textLength="273" lengthAdjust="spacingAndGlyphs">BIG FIGHT</text>
  </svg>
  <div class="brand"><span class="brand__dot"></span><span class="brand__name">BRIGHT PATH<br>ATTORNEYS</span></div>
  <div class="attorney" role="img" aria-label="Portrait of attorney Marla Benning, arms crossed, in a navy blazer"></div>
  <div class="rule"></div>
  <div class="phone">877-GRANTLY</div>
  <div class="web">brightpathlegalgroup.example</div>
</section>

<section class="billboard billboard--accident">
  <div class="scene scene--car" role="img" aria-label="Photo of a dark car on a road with bright sunlight behind"></div>
  <svg class="headline" viewBox="0 0 992 224">
    <text x="193" y="116" font-size="100" fill="var(--green)" textLength="437" lengthAdjust="spacingAndGlyphs">ACCIDENT?</text>
    <text x="193" y="183" font-size="61" fill="var(--green)" textLength="505" lengthAdjust="spacingAndGlyphs">NO FEE, UNLESS WE WIN!</text>
  </svg>
  <div class="brand"><span class="brand__dot"></span><span class="brand__name">BRIGHT PATH<br>ATTORNEYS</span></div>
  <div class="attorney" role="img" aria-label="Portrait of attorney Marla Benning, arms crossed, in a navy blazer"></div>
  <div class="rule"></div>
  <div class="phone">877-GRANTLY</div>
  <div class="web">brightpathlegalgroup.example</div>
</section>

<section class="billboard billboard--big-case">
  <div class="scene scene--truck" role="img" aria-label="Photo of a red semi truck seen from a low angle"></div>
  <svg class="headline" viewBox="0 0 992 224">
    <text x="208" y="99" font-size="80" fill="var(--yellow)" textLength="458" lengthAdjust="spacingAndGlyphs">BIG TRUCK. BIG CASE.</text>
    <text x="214" y="192" font-size="100" fill="var(--silver)" textLength="215" lengthAdjust="spacingAndGlyphs">YOU PAY</text>
    <text x="445" y="192" font-size="100" fill="var(--green)" textLength="65" lengthAdjust="spacingAndGlyphs">$0</text>
    <text x="523" y="192" font-size="100" fill="var(--silver)" textLength="244" lengthAdjust="spacingAndGlyphs">UPFRONT</text>
  </svg>
  <div class="brand"><span class="brand__dot"></span><span class="brand__name">BRIGHT PATH<br>ATTORNEYS</span></div>
  <div class="attorney" role="img" aria-label="Portrait of attorney Marla Benning, arms crossed, in a navy blazer"></div>
  <div class="rule"></div>
  <div class="phone">877-GRANTLY</div>
  <div class="web">brightpathlegalgroup.example</div>
</section>

</body>
</html>
```